Homepage Real Estate Agency

I need a web design for a real estate agency in Luxembourg. A short draft for the front page can be found in the project details. (Page 1+2) The main colors of the site should be blue as shown in the project details. (Page 3)
The main target for this site is to promote real estates and a small presentation of the company.

Industry/Entity Type

Real Estate

Requirements
Must have
• On the front page estates are shown in a short preview in small boxes, on the right side is a search. The search is hidden except for the front page. The header has 4 buttons and the logo of the company.

```html
<!DOCTYPE html>
<html lang="en">
<head>
<meta charset="utf-8">
<title>Valmont Homes – Real Estate</title>
<link rel="stylesheet" href="https://fonts.googleapis.com/css2?family=Arimo:wght@400;700&family=Cinzel:wght@400;600&family=Yanone+Kaffeesatz:wght@400;600&display=swap">
<style>
:root{
  --sky-top:#3f9fe0;
  --sky-bottom:#cfe9f7;
  --navy:#1c2f8c;
  --navy-deep:#0d2a5c;
  --nav-blue:#2438a8;
  --teal-dark:#2f5a5c;
  --teal-light:#a9c9c4;
  --panel-blue:#1f73c9;
  --red:#d41a1a;
  --green:#7cbf2a;
  --card-border:#dcdcdc;
  --text:#333;
  --white:#fff;
}
*{box-sizing:border-box;margin:0;padding:0}
html,body{width:828px;height:1200px;overflow:hidden;background:var(--white)}
body{position:relative;font-family:Arimo,Arial,sans-serif;color:var(--text)}
.abs{position:absolute}

/* header */
.sky{left:0;top:0;width:828px;height:118px;background:linear-gradient(180deg,var(--sky-top),var(--sky-bottom))}
.header-phone{left:613px;top:8px;display:flex;align-items:center;gap:8px;color:var(--white);font-size:17px;font-weight:700;letter-spacing:.5px}
.phone-dot{width:22px;height:22px;border-radius:50%;background:#e8f2fb;display:flex;align-items:center;justify-content:center}
.nav{left:312px;top:79px;width:471px;height:33px;background:linear-gradient(180deg,#3550c8,var(--nav-blue));border-radius:10px 10px 0 0;display:flex;justify-content:space-around;align-items:center}
.nav a{font-family:Cinzel,serif;color:var(--white);text-decoration:none;font-size:12.5px;padding:0 10px;border-right:1px solid rgba(255,255,255,.25);line-height:33px}
.nav a:last-child{border-right:none}
.header-rule{left:0;top:112px;width:828px;height:4px;background:var(--navy)}

/* hero */
.hero{left:0;top:116px;width:828px;height:366px;background:radial-gradient(ellipse at 30% 40%,var(--teal-light),var(--teal-dark) 75%)}
.brand-tab{left:68px;top:0;width:128px;height:118px;background:#e9e4d6}
.brand-badge{left:70px;top:60px;width:122px;height:122px;border-radius:50%;background:var(--white);border:10px solid var(--navy);display:flex;align-items:center;justify-content:center;font-size:17px;font-weight:700;color:var(--navy)}
.hero-title{left:46px;top:213px;width:260px;font-size:24px;line-height:27px;font-weight:700;color:var(--white);text-transform:uppercase;text-shadow:1px 1px 3px rgba(0,0,0,.4)}
.slider{left:312px;top:137px;width:474px;height:259px;background:#f4f0e6;padding:7px;box-shadow:0 2px 8px rgba(0,0,0,.4)}
.slider-photo{width:100%;height:100%;background:linear-gradient(180deg,#6fa8e0 0%,#bcd3ea 35%,#c9b99a 60%,#6f8a5a 85%,#3a8fc0 100%)}
.slider-arrow{top:263px;width:24px;height:24px;background:#1f8fd8;border:1px solid #0d5f9a}
.arrow-left{left:306px}.arrow-right{left:768px}
.skyline{left:0;top:389px;width:828px;height:93px;background:linear-gradient(180deg,rgba(120,150,160,.2),#5f6d78 55%,#93a87a 100%)}

/* listings */
.card{width:172px;height:266px;border:2px solid var(--card-border);border-radius:8px;background:var(--white);box-shadow:0 1px 4px rgba(0,0,0,.12)}
.card-photo{position:absolute;left:8px;top:10px;width:154px;height:131px;border-radius:8px;background:linear-gradient(180deg,#2f86d8 0%,#7ab4e6 40%,#8a5a44 55%,#6b4a3a 75%,#4f8a3a 100%)}
.card-facts{position:absolute;left:18px;top:153px;width:140px;font-size:9.5px;line-height:13.4px;display:grid;grid-template-columns:98px 1fr}
.card-facts dt{color:var(--text)}
.card-facts dd{color:var(--red)}
.more-btn{position:absolute;left:50%;bottom:-4px;transform:translateX(-50%);background:var(--red);color:var(--white);font-size:9.5px;padding:5px 8px;border-radius:3px 3px 0 0;white-space:nowrap}

/* search */
.search{left:619px;top:501px;width:172px;height:266px;border:2px solid var(--card-border);border-radius:8px;background:var(--white);padding:5px}
.search-inner{width:100%;height:100%;border-radius:6px;background:linear-gradient(180deg,#2a86d9,var(--panel-blue));padding:10px 12px}
.panel-title{font-family:"Yanone Kaffeesatz",sans-serif;font-size:18px;color:var(--white);letter-spacing:.5px;margin-bottom:14px}
.select{height:18px;background:var(--white);border-radius:2px;font-size:8px;color:#999;padding:0 6px;line-height:18px;margin-bottom:9px;position:relative}
.select::after{content:"";position:absolute;right:6px;top:7px;border:3px solid transparent;border-top-color:#333}
.radio{display:flex;align-items:center;gap:6px;font-size:8px;color:var(--white);margin:3px 0 0 6px}
.radio i{width:9px;height:9px;border-radius:50%;background:var(--white)}
.search-btn{margin-top:14px;width:87px;height:26px;border-radius:3px;background:linear-gradient(180deg,#9ad44a,#5a9e1c);color:var(--white);font-weight:700;font-size:13px;text-align:center;line-height:26px}

/* about */
.about{left:619px;top:792px;width:172px;height:266px;border:2px solid var(--card-border);border-radius:8px;background:var(--white);padding:10px 12px}
.about .panel-title{color:var(--navy-deep);margin-bottom:8px}
.about-photo{width:146px;height:82px;background:linear-gradient(180deg,#4e8fd6,#a9c6e2 50%,#8a96a4 100%)}
.about p{font-size:8px;line-height:11.3px;margin-top:10px;color:#222}
.read-more{text-align:right;font-size:8px;color:var(--red);margin-top:10px}

/* footer */
.footer{left:0;top:1095px;width:828px;height:105px;background:var(--navy-deep);color:var(--white)}
.foot-col{position:absolute;top:17px}
.foot-title{font-size:12.5px;letter-spacing:.3px}
.foot-line{display:flex;align-items:center;gap:10px;margin-top:12px;font-size:12px;color:#4fd13a}
.foot-line.small{margin-top:8px;font-size:10px}
.foot-icon{width:20px;height:16px;border-radius:50%;background:#6ab0ea}
.email-field{margin-top:12px;width:127px;height:19px;background:var(--white);color:#555;font-size:8px;padding:0 6px;line-height:19px}
.sub-btn{margin-top:5px;width:66px;height:18px;background:linear-gradient(180deg,#9ad44a,#5a9e1c);font-size:9px;font-weight:700;text-align:center;line-height:18px}
.social{display:flex;gap:12px;margin-top:12px}
.social span{width:34px;height:34px;border-radius:5px;background:#4a78c6}
.social span:nth-child(2){background:#3fb0e0}
.social span:nth-child(3){background:#2a6ab0}
.foot-brand{left:671px;top:14px;text-align:center}
.foot-badge{width:62px;height:62px;margin:0 auto 6px;border-radius:50%;background:var(--white);border:6px solid #3a2f8f}
.foot-name{font-size:12px;font-weight:700}
</style>
</head>
<body>
<header>
  <div class="abs sky"></div>
  <div class="abs header-phone"><span class="phone-dot"><svg width="10" height="12" viewBox="0 0 10 12"><path d="M2 0h2l1 3-1.5 1c.5 1.5 1.5 3 3 4L8 6.5l2 1v2c0 1-1 2.5-3 2C3 10 0 6 0 2 0 1 1 0 2 0z" fill="#1f5fb0"/></svg></span>352 555 0147</div>
  <nav class="abs nav"><a href="#">A VENDRE</a><a href="#">CONSTRUCTION</a><a href="#">LOCATION</a><a href="#">CHERCHONS</a></nav>
  <div class="abs header-rule"></div>
</header>

<section class="abs hero">
  <div class="abs hero-title" style="top:97px">Lorel ipsum dolor sit amet nuno Valencia esta di Maria</div>
</section>
<div class="abs brand-tab"></div>
<div class="abs brand-badge">Valmont</div>
<div class="abs slider"><div class="slider-photo" role="img" aria-label="Featured photo of a large multi-storey villa with pool"></div></div>
<div class="abs slider-arrow arrow-left"><svg width="22" height="22" viewBox="0 0 22 22"><path d="M14 6l-6 5 6 5z" fill="#fff"/></svg></div>
<div class="abs slider-arrow arrow-right"><svg width="22" height="22" viewBox="0 0 22 22"><path d="M8 6l6 5-6 5z" fill="#fff"/></svg></div>
<div class="abs skyline" role="img" aria-label="City skyline photograph"></div>

<main>
  <article class="abs card" style="left:47px;top:501px"><div class="card-photo" role="img" aria-label="Photo of a brick family house"></div><dl class="card-facts"><dt>City:</dt><dd>Portland</dd><dt>Beds:</dt><dd>4</dd><dt>Baths:</dt><dd>3.0</dd><dt>Square Feet:</dt><dd>4578</dd><dt>Area:</dt><dd>NW Jersy</dd><dt>Status:</dt><dd>Active</dd></dl><span class="more-btn">More Details</span></article>
  <article class="abs card" style="left:233px;top:501px"><div class="card-photo" role="img" aria-label="Photo of a brick family house"></div><dl class="card-facts"><dt>City:</dt><dd>Portland</dd><dt>Beds:</dt><dd>4</dd><dt>Baths:</dt><dd>3.0</dd><dt>Square Feet:</dt><dd>4578</dd><dt>Area:</dt><dd>NW Jersy</dd><dt>Status:</dt><dd>Active</dd></dl><span class="more-btn">More Details</span></article>
  <article class="abs card" style="left:419px;top:501px"><div class="card-photo" role="img" aria-label="Photo of a brick family house"></div><dl class="card-facts"><dt>City:</dt><dd>Portland</dd><dt>Beds:</dt><dd>4</dd><dt>Baths:</dt><dd>3.0</dd><dt>Square Feet:</dt><dd>4578</dd><dt>Area:</dt><dd>NW Jersy</dd><dt>Status:</dt><dd>Active</dd></dl><span class="more-btn">More Details</span></article>
  <article class="abs card" style="left:47px;top:792px"><div class="card-photo" role="img" aria-label="Photo of a brick family house"></div><dl class="card-facts"><dt>City:</dt><dd>Portland</dd><dt>Beds:</dt><dd>4</dd><dt>Baths:</dt><dd>3.0</dd><dt>Square Feet:</dt><dd>4578</dd><dt>Area:</dt><dd>NW Jersy</dd><dt>Status:</dt><dd>Active</dd></dl><span class="more-btn">More Details</span></article>
  <article class="abs card" style="left:233px;top:792px"><div class="card-photo" role="img" aria-label="Photo of a brick family house"></div><dl class="card-facts"><dt>City:</dt><dd>Portland</dd><dt>Beds:</dt><dd>4</dd><dt>Baths:</dt><dd>3.0</dd><dt>Square Feet:</dt><dd>4578</dd><dt>Area:</dt><dd>NW Jersy</dd><dt>Status:</dt><dd>Active</dd></dl><span class="more-btn">More Details</span></article>
  <article class="abs card" style="left:419px;top:792px"><div class="card-photo" role="img" aria-label="Photo of a brick family house"></div><dl class="card-facts"><dt>City:</dt><dd>Portland</dd><dt>Beds:</dt><dd>4</dd><dt>Baths:</dt><dd>3.0</dd><dt>Square Feet:</dt><dd>4578</dd><dt>Area:</dt><dd>NW Jersy</dd><dt>Status:</dt><dd>Active</dd></dl><span class="more-btn">More Details</span></article>

  <aside class="abs search">
    <div class="search-inner">
      <h2 class="panel-title">Search Your Dream Home</h2>
      <div class="select">Type Area</div>
      <div class="select">Type size of House</div>
      <div class="select">No of rooms</div>
      <div class="select">No of bathrooms</div>
      <div class="radio"><i></i>lorel impsum dolor sir</div>
      <div class="radio"><i></i>lorel impsum dolor sir</div>
      <div class="search-btn">SEARCH</div>
    </div>
  </aside>

  <aside class="abs about">
    <h2 class="panel-title">About Our Company</h2>
    <div class="about-photo" role="img" aria-label="Photo of a blue timber house"></div>
    <p>Lorem ipsum dolor sit amet, consectetur adipiscing elit. Praesent commodo convallis massa sed scelerisque. Morbi dignissim sem quis ligula venenatis elementum. Suspendisse neque diam, aliquam et tempus ut, adipiscing elementum felis.</p>
    <div class="read-more">Read More</div>
  </aside>
</main>

<footer class="abs footer">
  <div class="foot-col" style="left:48px">
    <div class="foot-title">FOR ANY QUERIES</div>
    <div class="foot-line"><span class="foot-icon"></span>352 555 0147</div>
    <div class="foot-line small"><span class="foot-icon" style="background:#3f9f6a"></span>info@valmonthomes.lu</div>
  </div>
  <div class="foot-col" style="left:253px">
    <div class="foot-title">SUBSCRIBE NEWSLETTER</div>
    <div class="email-field">Your email id</div>
    <div class="sub-btn">SUBMIT</div>
  </div>
  <div class="foot-col" style="left:520px">
    <div class="foot-title">GET IN TOUCH</div>
    <div class="social"><span aria-label="Social profile"></span><span aria-label="Social profile"></span><span aria-label="Social profile"></span></div>
  </div>
  <div class="foot-col foot-brand"><div class="foot-badge"></div><div class="foot-name">VALMONT HOMES</div></div>
</footer>
</body>
</html>
```